Kindred Light. a joyful state of being.

adding value to ones circumstance through the teachings of neutralization. quote for back of card: "and then it happens... One day you wake up and you're in this place. You are in this place where everything is right. Your heart is calm. Your soul is lit. Your thoughts are positive. Your vision is clear. Your faith is stronger than ever. And you are at peace. At peace with where you have been. At peace with what you've been through. And at peace with where you're headed." -unknown

Target Market(s)

spiritual, awakening, inspiration, motivation, gratefulness, oneness, peace, positive mindset,

Contact Information for Business Card

front: one line message from quote

Logo Text

up to suggestions

Font styles to use
Serif
Sans Serif
Script

Colors

Designer to choose colors to be used in the design.

Requirements
Must have
• entire quote on one side of card
Nice to have
• simple, and to the point
Should not have
• elaborated designs

```html
<!DOCTYPE html>
<html lang="en">
<head>
<meta charset="utf-8">
<title>Kindred Light — Identity &amp; Business Card</title>
<link rel="stylesheet" href="https://fonts.googleapis.com/css2?family=Cinzel:wght@400&family=Josefin+Sans:wght@300;600&family=Great+Vibes&display=swap">
<style>
  :root {
    --red: #ee1c25;
    --green: #2fa84a;
    --white: #ffffff;
    --ink: #444444;
    --stage: #ececec;
  }
  * { box-sizing: border-box; margin: 0; padding: 0; }
  html, body { width: 1200px; height: 1200px; overflow: hidden; }
  body {
    background: radial-gradient(ellipse at 50% 60%, #f7f7f7 0%, var(--stage) 75%);
    position: relative;
    font-family: "Josefin Sans", sans-serif;
  }

  /* Logo panels */
  .logo-panel {
    position: absolute; top: 0; width: 600px; height: 220px;
    display: flex; align-items: center; justify-content: center; gap: 14px;
  }
  .logo-panel--light { left: 0; background: var(--white); }
  .logo-panel--red { left: 600px; background: var(--red); }
  .brand-mark { width: 44px; height: 44px; border-radius: 50%; flex: none; }
  .brand-name {
    font-family: "Cinzel", serif; font-weight: 400; font-size: 38px;
    letter-spacing: 1px; line-height: 1; white-space: nowrap;
  }
  .logo-panel--light .brand-mark { background: var(--red); }
  .logo-panel--light .brand-name { color: var(--green); }
  .logo-panel--red .brand-mark { background: var(--white); width: 38px; height: 38px; }
  .logo-panel--red .brand-name { color: var(--white); font-size: 32px; }

  /* Cards */
  .card {
    position: absolute; left: 322px; width: 556px; height: 260px;
    box-shadow: 0 14px 30px rgba(0,0,0,0.12);
    overflow: hidden;
  }
  .card--back { top: 400px; background: var(--red); }
  .card--front { top: 756px; background: var(--white); }

  .back-disc {
    position: absolute; left: -120px; top: 40px;
    width: 240px; height: 240px; border-radius: 50%; background: var(--white);
  }
  .quote {
    position: absolute; left: 136px; width: 370px; top: 22px;
    color: var(--white); text-align: center;
  }
  .quote-rule { height: 1px; background: rgba(255,255,255,0.45); margin: 0 20px; }
  .quote-body {
    padding: 6px 0 6px; font-size: 13.4px; line-height: 16.4px;
    font-weight: 300; letter-spacing: 0.4px;
  }
  .quote-body strong { font-weight: 600; }
  .quote-lead { font-size: 17px; font-weight: 600; letter-spacing: 0.8px; line-height: 20px; }
  .quote-author {
    text-align: right; font-size: 15px; font-weight: 600; letter-spacing: 1px;
    margin-top: 8px; padding-right: 0;
  }

  .front-logo {
    position: absolute; top: 24px; left: 0; right: 0;
    display: flex; align-items: center; justify-content: center; gap: 10px;
  }
  .front-logo .brand-mark { width: 34px; height: 34px; background: var(--red); }
  .front-logo .brand-name { color: var(--green); font-size: 29px; }

  .name-row {
    position: absolute; top: 112px; left: 100px; right: 100px;
    border-top: 1px solid rgba(238,28,37,0.5); border-bottom: 1px solid rgba(238,28,37,0.5);
    padding: 5px 0; text-align: center; font-family: "Cinzel", serif;
  }
  .person-name { color: var(--red); font-size: 17px; letter-spacing: 4px; }
  .divider { color: var(--red); margin: 0 12px; }
  .person-title { color: var(--green); font-family: "Josefin Sans", sans-serif; font-weight: 600; font-size: 13px; letter-spacing: 2px; }

  .contact-row {
    position: absolute; top: 172px; left: 0; right: 0;
    display: flex; justify-content: center; gap: 16px;
    font-size: 11.5px; color: var(--ink); font-weight: 300; white-space: nowrap;
  }
  .contact-item { display: flex; align-items: center; gap: 5px; }
  .contact-icon { width: 15px; height: 15px; flex: none; }

  .tagline-row {
    position: absolute; top: 206px; left: 36px; right: 36px;
    display: flex; align-items: center; justify-content: space-between;
  }
  .leader { color: var(--red); font-size: 16px; letter-spacing: 6px; font-weight: 600; }
  .tagline { font-family: "Great Vibes", cursive; color: var(--green); font-size: 30px; white-space: nowrap; }
</style>
</head>
<body>

  <section class="logo-panel logo-panel--light">
    <span class="brand-mark"></span>
    <span class="brand-name">Kindred Light</span>
  </section>
  <section class="logo-panel logo-panel--red">
    <span class="brand-mark"></span>
    <span class="brand-name">Kindred Light</span>
  </section>

  <article class="card card--back">
    <div class="back-disc"></div>
    <div class="quote">
      <div class="quote-rule"></div>
      <p class="quote-body">
        <span class="quote-lead">“and then it happens...</span><br>
        One day you wake up and you're in this place.
        <strong>You are in this place where everything is right.</strong>
        Your heart is calm. <strong>Your soul is lit.</strong> Your thoughts are positive.
        <strong>Your vision is clear.</strong> Your faith is stronger than ever.
        <strong>And you are at peace. At peace with where you have been.</strong>
        At peace with what you've been through. <strong>And at peace with where you're headed.”</strong>
      </p>
      <div class="quote-rule"></div>
      <p class="quote-author">unknown</p>
    </div>
  </article>

  <article class="card card--front">
    <div class="front-logo">
      <span class="brand-mark"></span>
      <span class="brand-name">Kindred Light</span>
    </div>

    <div class="name-row">
      <span class="person-name">YOUR NAME</span><span class="divider">|</span><span class="person-title">Titel</span>
    </div>

    <div class="contact-row">
      <span class="contact-item">
        <svg class="contact-icon" viewBox="0 0 16 16"><circle cx="8" cy="8" r="8" fill="#ee1c25"/><path d="M5 4.5l1.5-.5 1 2-1 .8a5 5 0 0 0 2.7 2.7l.8-1 2 1-.5 1.5c-3.5.3-6.8-3-6.5-6.5z" fill="#fff"/></svg>
        000 000 555 019
      </span>
      <span class="contact-item">
        <svg class="contact-icon" viewBox="0 0 16 16"><circle cx="8" cy="8" r="8" fill="#ee1c25"/><rect x="4" y="5" width="8" height="6" fill="#fff"/><path d="M4 5l4 3.5L12 5" stroke="#ee1c25" stroke-width="1" fill="none"/></svg>
        hello@kindredlight.com
      </span>
      <span class="contact-item">
        <svg class="contact-icon" viewBox="0 0 16 16"><circle cx="8" cy="8" r="8" fill="#ee1c25"/><circle cx="8" cy="8" r="4" stroke="#fff" fill="none"/><path d="M4 8h8M8 4v8" stroke="#fff"/></svg>
        www.kindredlight.com
      </span>
    </div>

    <div class="tagline-row">
      <span class="leader">......</span>
      <span class="tagline">Your faith is stronger than ever</span>
      <span class="leader">......</span>
    </div>
  </article>

</body>
</html>
```